Industrial Automation company requires a business card design

Valtrin Automation provides design & build of Automated Equipment for manufacturing industry.
www.valtrinautomation.example
The equipment we design is used for manufacturing in sectors such as medical device, pharmaceutical, aerospace and electronics.
We require a new business card design which incorporates our (New) logo and the key message words:
Automated Equipment:
Design, Build, Control, Test, Support

```html
<!DOCTYPE html>
<html lang="en">
<head>
<meta charset="utf-8">
<title>Valtrin Automation – Business Card</title>
<link href="https://fonts.googleapis.com/css2?family=Montserrat:wght@400;500;600;700&display=swap" rel="stylesheet">
<style>
  :root {
    --backdrop: #2b2b2b;
    --card-black: #050505;
    --card-white: #ffffff;
    --brand-green: #0f8a3a;
    --ink: #1a1a1a;
    --muted: #333333;
  }
  * { box-sizing: border-box; margin: 0; padding: 0; }
  html, body {
    width: 1200px; height: 900px; overflow: hidden;
    background: var(--backdrop);
    font-family: "Montserrat", sans-serif;
  }
  .canvas { position: relative; width: 1200px; height: 900px; }

  .card {
    position: absolute;
    width: 700px; height: 400px;
    border-radius: 22px;
    overflow: hidden;
    box-shadow: 0 14px 30px rgba(0,0,0,.45);
  }

  /* Back side */
  .card-back { left: 90px; top: 40px; background: var(--card-black); color: #fff; }
  .card-back .brand-name {
    position: absolute; top: 120px; left: 0; right: 0;
    text-align: center; font-weight: 700; font-size: 54px; letter-spacing: 6px;
    color: #fff;
  }
  .card-back .tagline {
    position: absolute; top: 250px; left: 0; right: 0; text-align: center;
  }
  .tagline .tag-title { font-size: 17px; font-weight: 500; letter-spacing: .5px; }
  .tagline .tag-services { font-size: 17px; font-weight: 400; margin-top: 6px; }
  .tagline .dot { font-size: 12px; vertical-align: middle; margin: 0 3px; }
  .card-back .band-green {
    position: absolute; left: 0; bottom: 0; width: 64%; height: 30px;
    background: var(--brand-green);
  }
  .card-back .band-white {
    position: absolute; right: 0; bottom: 30px; width: 36%; height: 30px;
    background: var(--card-white);
  }
  .card-back .band-white-low {
    position: absolute; right: 0; bottom: 0; width: 36%; height: 30px;
    background: var(--card-white);
  }

  /* Front side */
  .card-front { left: 410px; top: 460px; background: var(--card-white); color: var(--ink); }
  .logo-lockup {
    position: absolute; left: 44px; top: 56px;
    display: flex; align-items: center; gap: 12px;
  }
  .logo-lockup .logo-square { width: 22px; height: 22px; background: var(--brand-green); }
  .logo-lockup .logo-name {
    font-weight: 700; font-size: 28px; letter-spacing: 1px; color: var(--ink);
  }
  .divider {
    position: absolute; left: 40px; right: 0; top: 200px;
    height: 2px; background: var(--brand-green);
  }
  .person {
    position: absolute; right: 50px; top: 160px; text-align: right;
  }
  .person .person-name {
    font-weight: 700; font-size: 26px; color: var(--brand-green); letter-spacing: .5px;
  }
  .person .person-role {
    margin-top: 10px; font-size: 14px; color: var(--muted);
  }
  .contact-list {
    position: absolute; left: 44px; top: 232px; list-style: none;
  }
  .contact-list li {
    display: flex; align-items: center; gap: 14px;
    font-size: 17px; line-height: 30px; color: var(--ink);
  }
  .contact-list svg { width: 16px; height: 16px; flex: none; }
  .contact-list .accent { color: var(--brand-green); }
  .card-front .band-black {
    position: absolute; left: 0; bottom: 0; width: 66%; height: 22px;
    background: var(--card-black);
  }
  .card-front .band-green {
    position: absolute; right: 0; bottom: 0; width: 34%; height: 40px;
    background: var(--brand-green);
  }
</style>
</head>
<body>
<div class="canvas">

  <section class="card card-back" aria-label="Card back">
    <div class="brand-name">VALTRIN</div>
    <div class="tagline">
      <p class="tag-title">AUTOMATED EQUIPMENT:</p>
      <p class="tag-services">Design<span class="dot">●</span>Build<span class="dot">●</span>Control<span class="dot">●</span>Test<span class="dot">●</span>Support</p>
    </div>
    <div class="band-white"></div>
    <div class="band-white-low"></div>
    <div class="band-green"></div>
  </section>

  <section class="card card-front" aria-label="Card front">
    <div class="logo-lockup">
      <span class="logo-square"></span>
      <span class="logo-name">VALTRIN AUTOMATION</span>
    </div>

    <div class="person">
      <p class="person-name">MAREK HOLLOWAY</p>
    </div>
    <div class="divider"></div>
    <div class="person" style="top:210px">
      <p class="person-role">Director</p>
    </div>

    <ul class="contact-list">
      <li>
        <svg viewBox="0 0 16 16"><rect x="4" y="1" width="8" height="14" rx="1.5" fill="none" stroke="#0f8a3a" stroke-width="1.6"/><circle cx="8" cy="12.5" r="0.9" fill="#0f8a3a"/></svg>
        123-456-7890
      </li>
      <li>
        <svg viewBox="0 0 16 16"><path d="M3 2l3 0 1 3-2 1.5a8 8 0 0 0 4.5 4.5L11 9l3 1v3a1 1 0 0 1-1 1A12 12 0 0 1 2 3a1 1 0 0 1 1-1z" fill="#0f8a3a"/></svg>
        +330-2460-0142
      </li>
      <li>
        <svg viewBox="0 0 16 16"><circle cx="8" cy="8" r="6.5" fill="none" stroke="#0f8a3a" stroke-width="1.4"/><ellipse cx="8" cy="8" rx="3" ry="6.5" fill="none" stroke="#0f8a3a" stroke-width="1.2"/><line x1="1.5" y1="8" x2="14.5" y2="8" stroke="#0f8a3a" stroke-width="1.2"/></svg>
        info@valtrinautomation.example
      </li>
      <li>
        <svg viewBox="0 0 16 16"><rect x="1.5" y="3.5" width="13" height="9" rx="1" fill="none" stroke="#0f8a3a" stroke-width="1.4"/><path d="M1.5 4l6.5 5 6.5-5" fill="none" stroke="#0f8a3a" stroke-width="1.4"/></svg>
        <span>www.<span class="accent">valtrinautomation</span>.example</span>
      </li>
    </ul>

    <div class="band-black"></div>
    <div class="band-green"></div>
  </section>

</div>
</body>
</html>
```